Tidal Coatings business card for residential and commercial painting

A clean, professional design. Easy to read
Eye catching and elegant
Front could have some color variations
On the back of card I would like all black with signature logo

*Attached is my current business card and the items I want displayed

Contact Information for Business Card

Email, phone number, website, and owner name

Font styles to use
Serif

Requirements
Must have
• My logo with cool design and perhaps some paint splatter

```html
<!DOCTYPE html>
<html lang="en">
<head>
<meta charset="UTF-8">
<title>Tidal Coatings – Business Card</title>
<link rel="stylesheet" href="https://fonts.googleapis.com/css2?family=Oswald:wght@400;500&family=Arimo:wght@400&display=swap">
<style>
  :root {
    --canvas-bg: #e9e7e4;
    --card-dark: #3a3a3c;
    --brand-blue: #1a78c2;
    --text-light: #ffffff;
    --wordmark: #2f3033;
    --field-white: #ffffff;
  }
  * { margin: 0; padding: 0; box-sizing: border-box; }
  html, body {
    width: 1200px; height: 900px; overflow: hidden;
    background: var(--canvas-bg);
  }
  .card {
    position: absolute; left: 100px; top: 141px;
    width: 1000px; height: 618px;
    background: var(--card-dark);
    overflow: hidden;
    box-shadow: 0 10px 30px rgba(0,0,0,0.18);
  }
  .accent-band {
    position: absolute; left: 721px; top: 0;
    width: 279px; height: 100%;
    background: var(--brand-blue);
  }
  .owner-name {
    position: absolute; left: 44px; top: 74px;
    font-family: "Oswald", sans-serif; font-weight: 400;
    font-size: 56px; line-height: 1; letter-spacing: -0.5px;
    color: var(--brand-blue);
  }
  .owner-title {
    position: absolute; left: 42px; top: 134px;
    font-family: "Arimo", sans-serif; font-size: 28px;
    color: var(--text-light);
  }
  .price-row {
    position: absolute; left: 44px; top: 278px;
    display: flex; align-items: center; gap: 14px;
  }
  .price-label {
    font-family: "Oswald", sans-serif; font-size: 40px;
    color: var(--brand-blue); line-height: 1;
  }
  .price-field {
    width: 271px; height: 62px; background: var(--field-white);
  }
  .contact-list {
    position: absolute; left: 42px; top: 438px;
    list-style: none;
    font-family: "Arimo", sans-serif; font-size: 28px;
    color: var(--text-light);
  }
  .contact-list li {
    display: flex; align-items: center; gap: 14px; height: 36px;
  }
  .contact-list svg { width: 32px; height: 32px; flex: none; }
  .logo-disc {
    position: absolute; left: 446px; top: 51px;
    width: 526px; height: 526px; border-radius: 50%;
    background: radial-gradient(circle at 45% 40%, #f4f0ef 0%, #dcd5d5 45%, #c7b9bb 75%, #b9a6a8 100%);
  }
  .wordmark {
    position: absolute; left: 446px; top: 51px;
    width: 526px; height: 526px;
    display: flex; align-items: center; justify-content: center;
    font-family: "Oswald", sans-serif; font-weight: 500;
    font-size: 66px; letter-spacing: 1px;
    color: var(--wordmark);
  }
</style>
</head>
<body>
  <div class="card">
    <div class="accent-band"></div>

    <h1 class="owner-name">Marcus "Mack"</h1>
    <p class="owner-title">Owner-Licensed &amp; Insured</p>

    <div class="price-row">
      <span class="price-label">Price:</span>
      <span class="price-field"></span>
    </div>

    <ul class="contact-list">
      <li>
        <svg viewBox="0 0 32 32" aria-hidden="true"><path d="M9 4l5 6-3 3c1.5 3.5 4.5 6.5 8 8l3-3 6 5-3 5C15 27 5 17 4 7z" fill="none" stroke="#1a78c2" stroke-width="2.4" stroke-linejoin="round"/></svg>
        555.204.3187
      </li>
      <li>
        <svg viewBox="0 0 32 32" aria-hidden="true"><rect x="2" y="8" width="28" height="18" fill="#1a78c2"/><path d="M2 8l14 11L30 8" fill="none" stroke="#3a3a3c" stroke-width="2"/></svg>
        tidalcoatingstn@mail.com
      </li>
      <li>
        <svg viewBox="0 0 32 32" aria-hidden="true"><g fill="none" stroke="#1a78c2" stroke-width="2"><circle cx="16" cy="16" r="13"/><ellipse cx="16" cy="16" rx="6" ry="13"/><path d="M3 16h26M5 9h22M5 23h22"/></g></svg>
        www.tidalcoatingstn.com
      </li>
    </ul>

    <div class="logo-disc" role="img" aria-label="Frosted circular panel behind the company name"></div>
    <div class="wordmark">TIDAL COATINGS</div>
  </div>
</body>
</html>
```